Business Card Design Project

I have attached the logo and the colour pallete for the branding for the company.

Creative designs for business cards are needed.

The Company is modern corporate.

Industry/Entity Type

Business

```html
<!DOCTYPE html>
<html lang="en">
<head>
<meta charset="UTF-8">
<title>Routely Business Card</title>
<link rel="stylesheet" href="https://fonts.googleapis.com/css2?family=Montserrat:wght@300;400;600;700&display=swap">
<style>
  :root {
    --plum: #5c1f5a;
    --plum-deep: #3f1a43;
    --plum-mid: #6a2766;
    --orange: #e8771e;
    --paper: #f1f0ef;
    --backdrop: #e4e1de;
    --ink-soft: #6b3a68;
  }
  * { margin: 0; padding: 0; box-sizing: border-box; }
  html, body { width: 1200px; height: 900px; overflow: hidden; }
  body {
    background: var(--backdrop);
    font-family: "Montserrat", Arial, sans-serif;
    display: flex;
    align-items: center;
    justify-content: center;
    gap: 90px;
  }
  .card {
    width: 340px;
    height: 595px;
    border-radius: 4px;
    box-shadow: 0 10px 30px rgba(0,0,0,0.12);
    position: relative;
    overflow: hidden;
  }
  .card-front { background: var(--paper); padding: 58px 44px 0 44px; color: var(--plum); }
  .brand { display: flex; align-items: center; gap: 10px; }
  .brand-name { font-size: 40px; font-weight: 600; letter-spacing: -0.5px; color: var(--plum); line-height: 1; }
  .brand-dot { width: 14px; height: 14px; border-radius: 50%; background: var(--orange); }
  .rule { border: 0; border-top: 2px dotted var(--ink-soft); margin: 30px 0; opacity: 0.8; }
  .person-name { font-size: 19px; font-weight: 700; letter-spacing: 0.5px; text-transform: uppercase; }
  .person-role { font-size: 15px; font-weight: 400; margin-top: 2px; color: var(--ink-soft); }
  .contact { list-style: none; font-size: 15px; font-weight: 300; line-height: 1.45; }
  .contact li { display: flex; gap: 14px; }
  .contact .label { width: 14px; font-weight: 400; }
  .address { margin-top: 34px; font-size: 15px; font-weight: 300; line-height: 1.4; }
  .website { margin-top: 40px; font-size: 15px; font-weight: 400; color: var(--orange); }
  .card-back {
    background: radial-gradient(circle at 55% 35%, var(--plum-mid), var(--plum-deep) 85%);
    display: flex; align-items: center; justify-content: center;
  }
  .back-brand { display: flex; align-items: center; gap: 14px; margin-top: -60px; }
  .back-brand .brand-name { font-size: 54px; color: #ffffff; }
  .back-brand .brand-dot { width: 20px; height: 20px; }
  .back-url {
    position: absolute; bottom: 34px; right: 30px;
    font-size: 15px; font-weight: 300; color: #ffffff; letter-spacing: 0.3px;
  }
</style>
</head>
<body>
  <section class="card card-front">
    <div class="brand">
      <span class="brand-name">Routely</span>
      <span class="brand-dot"></span>
    </div>
    <hr class="rule">
    <p class="person-name">Daniel Reed Morgan</p>
    <p class="person-role">Founder &amp; CEO</p>
    <hr class="rule">
    <ul class="contact">
      <li><span class="label">T</span><span>555 014 2290</span></li>
      <li><span class="label">M</span><span>555 014 2290</span></li>
      <li><span class="label">E</span><span>daniel@routely.com</span></li>
    </ul>
    <p class="address">Calle Olmo 12. Col. Centro<br>City DF 01020. MX.</p>
    <p class="website">www.routely.com</p>
  </section>

  <section class="card card-back">
    <div class="back-brand">
      <span class="brand-name">Routely</span>
      <span class="brand-dot"></span>
    </div>
    <p class="back-url">www.routely.com</p>
  </section>
</body>
</html>
```